Corbel Path Advisory WordPress Design

Corbel Path Advisory is a consulting company that targets small business. We use our genius in the field to help small Business navigate information systems, in particular Tallybridge Solutions.

We are looking for a WordPress Design that is playful but intelligent for our web site. The design should plays off of our Corbel Logo and be informative. The attachments is of our logo variations that will be used in your design. It should be useful to describe the look and feel of the site we are looking to get.

The color of the website is not defined yet but should work well with our logo colors.

Regarding to the template and the way to display the home page. The menu should contain the following items which will each be its own page:
1. Home Page
2. Blog
-This needs to be a frame work to allow us to constantly add written articles and Video logs with Transcripts possibly in two sections.
3. What Corbel Does
-This will contain the company approach
4. Request a Corbel
-This will be a form to collect contact information
5. Contact Corbel
6. About Us

Please keep the SIMILAR airy/mythical design used in the logo.

Finally, we need a design that will have a normal view and a mobile view.

Target Market(s)

Corbel Path Advisory is a consulting company that targets small business.

Industry/Entity Type

Business Consultant

Requirements
Must have
• Regarding to the template and the way to display the home page. The menu should contain the following items which will each be its own page:
• 1. Home Page
• 2. Blog
• -This needs to be a frame work to allow us to constantly add written articles and Video logs with Transcripts possibly in two sections.
• 3. What Corbel Does
• -This will contain the company approach
• 4. Request a Corbel
• -This will be a form to collect contact information
• 5. Contact Corbel
• 6. About Us
• Mobile View
Nice to have
• Have a magical or mythical quality like the hands around the logo but not to playful.
Should not have
• Our slogan is "Corbel solutions that make business work!"

```html
<!DOCTYPE html>
<html lang="en">
<head>
<meta charset="utf-8">
<meta name="viewport" content="width=device-width, initial-scale=1">
<title>Corbel Path Advisory</title>
<link href="https://fonts.googleapis.com/css2?family=Open+Sans:wght@400;600;700&family=Oswald:wght@400;600&family=Rambla:wght@400;700&display=swap" rel="stylesheet">
<style>
:root{
  --sky-top:#3f8fd6;
  --sky-mid:#9fd0f2;
  --sky-low:#e9f5fc;
  --navy:#163f78;
  --blue:#1f6fc1;
  --parchment:#f4d98e;
  --parchment-dark:#e2b85a;
  --orange:#e8891c;
  --orange-dark:#c76a0a;
  --brown:#5a3a14;
  --brown-dark:#3e2608;
  --text:#4a3b26;
  --white:#ffffff;
}
*{margin:0;padding:0;box-sizing:border-box}
html,body{width:1200px;height:2252px;overflow:hidden}
body{
  position:relative;
  font-family:"Open Sans",sans-serif;
  color:var(--text);
  background:linear-gradient(180deg,var(--sky-top) 0,var(--sky-mid) 260px,var(--sky-low) 900px,#cfe6f6 1600px,#9cc9ea 2252px);
}
.abs{position:absolute}
/* top bar */
.topbar{top:14px;left:180px;width:840px;height:28px;font-size:15px;color:var(--white);display:flex;justify-content:space-between;align-items:center}
.topbar span{display:flex;align-items:center;gap:8px;font-weight:600}
.topbar .phone{font-size:20px;font-weight:700}
.brand{top:48px;left:440px;display:flex;align-items:center;gap:16px}
.brand-mark{width:92px;height:92px;border-radius:50%;background:var(--white);opacity:.9;flex:none}
.brand-name{font-family:"Rambla",sans-serif;font-weight:700;font-size:40px;color:var(--navy);line-height:1}
/* nav */
.nav{top:208px;left:180px;width:840px;height:34px;background:linear-gradient(180deg,#3a2412,#5b3c1a);border-radius:4px;display:flex;align-items:center;justify-content:center;gap:34px;font-family:"Oswald",sans-serif;font-size:16px;letter-spacing:1px}
.nav a{color:#f6e7c7;text-decoration:none;text-transform:uppercase}
.nav a.active{background:var(--white);color:var(--brown-dark);padding:2px 12px;border-radius:3px}
/* hero */
.hero{top:252px;left:0;width:1200px;height:448px;background:linear-gradient(120deg,#9cb6cc 0,#d8e3ec 40%,#5a6f86 70%,#2e3c52 100%)}
.hero-card{top:332px;left:200px;width:280px;padding:14px 18px;background:rgba(30,110,195,.92);color:var(--white);font-family:"Oswald",sans-serif;font-size:26px;line-height:1.25;font-style:italic;text-transform:uppercase}
.hero-card p{font-family:"Open Sans",sans-serif;font-style:normal;text-transform:none;font-size:12px;margin-top:8px;line-height:1.4}
.dots{top:668px;left:210px;display:flex;gap:8px}
.dots i{width:12px;height:12px;border-radius:50%;background:rgba(255,255,255,.6)}
.dots i:first-child{background:var(--white)}
/* panel */
.panel{top:712px;left:160px;width:880px;height:1368px;background:linear-gradient(180deg,#f7e2a2,var(--parchment) 40%,#f1cf7a);border:2px solid var(--parchment-dark);box-shadow:0 0 30px rgba(0,0,0,.15)}
.features{top:724px;left:170px;width:860px;display:flex}
.feature{flex:1;text-align:center;padding:0 26px}
.feature svg{width:54px;height:54px}
.feature h3{font-family:"Oswald",sans-serif;font-weight:400;font-size:30px;color:var(--white);line-height:1.05;text-shadow:0 1px 2px rgba(120,80,20,.5)}
.feature h3.blue{color:var(--blue);text-shadow:none}
.feature h4{font-size:12px;color:var(--orange-dark);font-weight:700;margin:6px 0;text-transform:uppercase}
.feature p{font-size:12px;line-height:1.5;color:var(--text);height:72px}
.btn{display:inline-block;margin-top:12px;padding:6px 18px;background:linear-gradient(180deg,#f6a23c,var(--orange-dark));color:var(--white);font-size:11px;font-weight:700;border-radius:3px;text-transform:uppercase}
.welcome{top:1036px;left:200px;width:800px;height:120px;background:linear-gradient(180deg,#fbfdff,#d9e9f6);border:1px solid #b9cfe4;border-radius:6px;display:flex;align-items:center;padding:0 30px;gap:26px}
.welcome h2{font-family:"Oswald",sans-serif;font-weight:600;font-size:64px;color:var(--navy)}
.welcome p{font-size:15px;color:var(--blue);font-weight:600;line-height:1.4}
.cols{top:1192px;left:190px;width:820px;display:flex;gap:30px}
.col{flex:1}
.col h3{font-family:"Oswald",sans-serif;font-weight:400;font-size:32px;color:var(--brown);line-height:1.05}
.teach-head{display:flex;gap:12px;align-items:center}
.portrait{width:96px;height:96px;border-radius:50%;background:linear-gradient(180deg,#c9b39a,#6b4e38);flex:none}
.teach-head h3{font-size:24px;color:var(--orange-dark)}
.col p{font-size:11.5px;line-height:1.55;margin-top:10px}
.news{display:flex;gap:12px;margin-top:16px}
.news .d{width:44px;flex:none;font-family:"Oswald",sans-serif;font-size:42px;color:var(--orange-dark);line-height:.9;text-align:center}
.news .d small{display:block;font-size:11px;color:var(--brown)}
.news h5{font-size:15px;color:var(--brown);font-weight:600}
.news p{margin-top:2px}
.services{list-style:none;margin-top:12px}
.services li{font-size:13px;font-weight:600;color:var(--brown);text-transform:uppercase;padding:3px 0;border-bottom:1px dotted #c9a45a}
.steps{top:1604px;left:200px;width:800px;display:flex;justify-content:space-between}
.step{width:120px;text-align:center;font-family:"Oswald",sans-serif;font-size:14px;color:var(--brown)}
.step .fig{width:100px;height:140px;margin:0 auto 8px;background:radial-gradient(ellipse at 50% 60%,#3d7fcf,#1c4f93 70%,transparent 72%)}
.quote{top:1804px;left:200px;width:800px;height:130px;background:linear-gradient(180deg,#6a4418,var(--brown-dark));border-radius:14px;display:flex;align-items:center;gap:22px;padding:0 26px}
.badge{width:84px;height:84px;border-radius:50%;background:#f5b52a;color:var(--brown-dark);font-family:"Oswald",sans-serif;font-weight:600;font-size:28px;display:flex;align-items:center;justify-content:center;flex:none}
.quote-text{flex:1;min-width:0}
.quote h3{font-family:"Oswald",sans-serif;font-weight:400;font-size:25px;line-height:1.2;color:#f5c24a;white-space:nowrap}
.quote p{font-size:12px;line-height:1.45;color:#f2e3c3;margin-top:4px}
.quote .cta{flex:none;background:linear-gradient(180deg,#3f8fe0,#1a5fae);color:var(--white);font-weight:700;font-size:13px;padding:14px 18px;border-radius:4px;white-space:nowrap;text-transform:uppercase}
.footer{top:1960px;left:162px;width:876px;height:118px;background:linear-gradient(180deg,#c58f34,#a56f1c);display:flex;padding:16px 40px;gap:60px}
.footer ul{list-style:none}
.footer li{font-size:13px;color:#fff6df;padding:2px 0}
.footer li::before{content:"\203A";margin-right:8px;color:#ffe29a}
.footer .brand-foot{margin-left:auto;display:flex;align-items:center;gap:10px}
.footer .brand-foot .brand-mark{width:60px;height:60px}
.footer .brand-foot span{font-family:"Rambla",sans-serif;font-weight:700;font-size:22px;color:var(--white);line-height:1.1;width:150px}
.copy{top:2120px;left:162px;width:876px;font-size:12px;color:var(--navy)}

/* mobile view */
@media (max-width:640px){
  html,body{width:100%;height:auto;overflow-x:hidden;overflow-y:auto}
  body{padding-bottom:24px}
  .abs{position:static;width:auto;left:auto;top:auto}
  .topbar{height:auto;flex-direction:column;gap:4px;padding:12px 16px}
  .topbar .phone{font-size:17px}
  .brand{justify-content:center;padding:10px 16px}
  .brand-mark{width:56px;height:56px}
  .brand-name{font-size:26px}
  .nav{height:auto;flex-wrap:wrap;gap:8px 16px;margin:10px 12px;padding:10px;font-size:14px}
  .hero{height:220px}
  .hero-card{width:auto;margin:-60px 16px 0;position:relative;font-size:20px}
  .dots{display:none}
  .panel{display:none}
  .features,.welcome,.cols,.steps,.quote,.footer{margin:16px 12px;background-color:var(--parchment)}
  .features{flex-direction:column;gap:24px;padding:20px 0;border-radius:6px}
  .feature p{height:auto}
  .welcome{height:auto;flex-direction:column;padding:16px;gap:8px;text-align:center}
  .welcome h2{font-size:40px}
  .cols{flex-direction:column;gap:24px;padding:16px;border-radius:6px}
  .steps{flex-wrap:wrap;justify-content:center;gap:12px;padding:16px;border-radius:6px}
  .step{width:90px}
  .step .fig{width:70px;height:100px}
  .quote{height:auto;flex-direction:column;text-align:center;padding:20px 16px;background:linear-gradient(180deg,#6a4418,var(--brown-dark))}
  .quote h3{white-space:normal;font-size:22px}
  .footer{height:auto;flex-direction:column;gap:12px;padding:16px 20px;background:linear-gradient(180deg,#c58f34,#a56f1c)}
  .footer .brand-foot{margin-left:0}
  .copy{padding:0 16px;text-align:center}
}
</style>
</head>
<body>
<div class="abs topbar">
  <span><svg width="18" height="14" viewBox="0 0 18 14"><rect x="1" y="1" width="16" height="12" fill="none" stroke="#fff" stroke-width="2"/><path d="M1 1l8 7 8-7" fill="none" stroke="#fff" stroke-width="2"/></svg>hello@corbelpath.example</span>
  <span class="phone"><svg width="18" height="18" viewBox="0 0 24 24"><path d="M6 2l4 4-2 3a12 12 0 007 7l3-2 4 4-3 4C10 22 2 14 2 5z" fill="#fff"/></svg>0161 555 0142</span>
</div>
<div class="abs brand">
  <div class="brand-mark"></div>
  <div class="brand-name">Corbel Path Advisory</div>
</div>
<nav class="abs nav">
  <a class="active">Home</a><a>Blog</a><a>What Corbel Does</a><a>Request a Corbel</a><a>Contact Corbel</a><a>About Us</a>
</nav>
<div class="abs hero" role="img" aria-label="Photo of business people reviewing documents at a desk, city skyline behind"></div>
<div class="abs hero-card">Lorem ipsum dolor sitafot<p>Sed ut perspiciatis unde omnis iste natus error sit voluptatem accusantium doloremque.</p></div>
<div class="abs dots"><i></i><i></i><i></i><i></i></div>

<div class="abs panel"></div>
<section class="abs features">
  <div class="feature">
    <svg viewBox="0 0 54 54"><rect x="8" y="30" width="8" height="16" fill="#c76a0a"/><rect x="22" y="20" width="8" height="26" fill="#c76a0a"/><rect x="36" y="10" width="8" height="36" fill="#c76a0a"/></svg>
    <h3>Finance<br>Management</h3><h4>Lorem ipsum dolor sitamet</h4>
    <p>Sed ut perspiciatis unde omnis iste natus error sit voluptatem accusantium doloremque laudantium totam rem aperiam eaque ipsa.</p>
    <span class="btn">Read more</span>
  </div>
  <div class="feature">
    <svg viewBox="0 0 54 54"><circle cx="27" cy="15" r="9" fill="#c76a0a"/><path d="M10 48c0-12 8-18 17-18s17 6 17 18z" fill="#c76a0a"/></svg>
    <h3>Skills<br>&amp; Employment</h3><h4>Lorem ipsum dolor sitamet</h4>
    <p>Nemo enim ipsam voluptatem quia voluptas sit aspernatur aut odit aut fugit sed quia consequuntur magni dolores eos qui.</p>
    <span class="btn">Read more</span>
  </div>
  <div class="feature">
    <svg viewBox="0 0 54 54"><circle cx="27" cy="27" r="19" fill="none" stroke="#1f6fc1" stroke-width="4"/><path d="M8 27h38M27 8c-10 10-10 28 0 38M27 8c10 10 10 28 0 38" fill="none" stroke="#1f6fc1" stroke-width="3"/></svg>
    <h3 class="blue">Outsourcing<br>Programs</h3><h4>Lorem ipsum dolor sitamet</h4>
    <p>Neque porro quisquam est qui dolorem ipsum quia dolor sit amet consectetur adipisci velit sed quia non numquam eius.</p>
    <span class="btn">Read more</span>
  </div>
</section>
<div class="abs welcome"><h2>WELCOME!</h2><p>Lorem ipsum dolor sit amet, consectetur adipiscing elit. Sed do eiusmod tempor incididunt ut labore et dolore magna aliqua.</p></div>

<section class="abs cols">
  <div class="col">
    <div class="teach-head"><div class="portrait" role="img" aria-label="Portrait photo of a consultant"></div><h3>We Teach You How To Implement!</h3></div>
    <p>Sed ut perspiciatis unde omnis iste natus error sit voluptatem accusantium doloremque laudantium, totam rem aperiam, eaque ipsa quae ab illo inventore veritatis et quasi architecto beatae vitae dicta sunt explicabo. Nemo enim ipsam voluptatem quia voluptas sit aspernatur aut odit aut fugit, sed quia consequuntur magni dolores eos qui ratione voluptatem sequi nesciunt neque porro quisquam.</p>
  </div>
  <div class="col">
    <h3>What's New</h3>
    <div class="news"><div class="d">22<small>JULY</small></div><div><h5>Sed ut perspiciu</h5><p>Totam rem aperiam eaque ipsa quae ab illo.</p></div></div>
    <div class="news"><div class="d">15<small>JULY</small></div><div><h5>Sed ut perspiciu</h5><p>Nemo enim ipsam voluptatem quia voluptas sit.</p></div></div>
    <div class="news"><div class="d">09<small>JULY</small></div><div><h5>Sed ut perspiciu</h5><p>Neque porro quisquam est qui dolorem ipsum.</p></div></div>
  </div>
  <div class="col">
    <h3>Our Services</h3>
    <ul class="services"><li>Implementation</li><li>SEO</li><li>SEO Marketing</li><li>IT &amp; E-Commerce</li><li>Sales and Marketing</li><li>Exploit Your Ideas</li><li>Market Sales</li><li>Assessment Plan</li><li>Strategy Plan</li><li>Manage Research</li></ul>
  </div>
</section>

<section class="abs steps">
  <div class="step"><div class="fig" role="img" aria-label="Blue figure illustration searching"></div>SEARCH</div>
  <div class="step"><div class="fig" role="img" aria-label="Blue figure illustration analysing"></div>ANALYSE</div>
  <div class="step"><div class="fig" role="img" aria-label="Blue figure illustration identifying"></div>IDENTIFY</div>
  <div class="step"><div class="fig" role="img" aria-label="Blue figure illustration developing"></div>DEVELOP</div>
  <div class="step"><div class="fig" role="img" aria-label="Blue figure illustration celebrating success"></div>SUCCESS</div>
</section>

<div class="abs quote">
  <div class="badge">24h</div>
  <div class="quote-text"><h3>Have a question or need a custom quote?</h3><p>Lorem ipsum dolor sit amet, consectetur adipiscing elit, sed do eiusmod tempor incididunt ut labore.</p></div>
  <span class="cta">Get started now for free</span>
</div>

<footer class="abs footer">
  <ul><li>Developer</li><li>Tools</li><li>Our Menu</li><li>Business Help</li></ul>
  <ul><li>About Us</li><li>Services</li><li>Our Staff</li><li>Events &amp; Press</li></ul>
  <ul><li>Contact Us</li><li>Education &amp; Training</li><li>Affiliate Program</li><li>Privacy Item</li></ul>
  <div class="brand-foot"><div class="brand-mark"></div><span>Corbel Path Advisory</span></div>
</footer>
<div class="abs copy">© 2024 Corbel Path Advisory. All rights reserved.</div>
</body>
</html>
```